Sticker Design for Company Equipment - Velunora

We are looking for a professional and clean graphic design for a set of stickers to apply on our company equipment (cleaning, gardening, pest control). The stickers must include our logo (the square with the three colored segments and the checkmark), our phone number, email address, and website, you can decide to use all three or just our website based on your graphic needs. It is important that it has an attractive sharp and clear look. The design should be consistent with our brand identity and give a polished, trustworthy look to our tools and machinery. We need a modular design that works in different formats (rectangular, square, round), depending on the type of equipment.

Need extra days to review

```html
<!DOCTYPE html>
<html lang="en">
<head>
<meta charset="utf-8">
<title>Velunora – Equipment Sticker Set</title>
<link href="https://fonts.googleapis.com/css2?family=Montserrat:wght@500;600;700&display=swap" rel="stylesheet">
<style>
:root{
  --navy:#0b0a6b;
  --green:#6ecf2f;
  --orange:#ff6a0a;
  --paper:#ffffff;
  --cut:#555555;
  --font:"Montserrat", Arial, sans-serif;
}
*{box-sizing:border-box;margin:0;padding:0}
html,body{width:1200px;height:848px;overflow:hidden;background:var(--paper)}
body{position:relative;font-family:var(--font);color:var(--navy)}
.sticker{position:absolute;background:var(--paper);border:1px solid var(--cut)}
.brand{display:flex;align-items:center}
.brand-square{background:var(--navy);flex:none}
.brand-name{font-weight:700;color:var(--navy);line-height:1;letter-spacing:.01em}
.tagline{font-weight:600;letter-spacing:.12em;white-space:nowrap;line-height:1}
.tagline .t-clean{color:var(--navy)}
.tagline .t-garden{color:var(--green)}
.tagline .t-pest{color:var(--orange)}
.icon{flex:none;fill:none;stroke:var(--navy);stroke-width:1.8;stroke-linecap:round;stroke-linejoin:round}
.contact-line{display:flex;align-items:center;justify-content:center;gap:8px;font-weight:500;white-space:nowrap}

/* round sticker */
.round{left:97px;top:283px;width:282px;height:282px;border-radius:50%}
.round .rings{position:absolute;inset:-1px}
.round .brand-square{position:absolute;left:113px;top:53px;width:56px;height:56px}
.round .brand-name{position:absolute;left:0;right:0;top:125px;text-align:center;font-size:32px}
.round .tagline{position:absolute;left:0;right:0;top:158px;text-align:center;font-size:9.3px}
.round .contacts{position:absolute;left:0;right:0;top:175px;display:flex;flex-direction:column;gap:3px;font-size:14px}

/* small framed cards */
.card{left:442px;width:244px;height:160px}
.card-navy{top:74px}
.card-green{top:242px}
.card-orange{top:409px}
.card .frame{position:absolute;inset:9px;border:3px solid var(--navy)}
.card-green .frame{border-color:var(--green)}
.card-orange .frame{border-color:var(--orange)}
.card .brand{position:absolute;left:20px;top:28px;gap:8px}
.card .brand-square{width:33px;height:33px}
.card .brand-name{font-size:27px}
.card .tagline{position:absolute;left:61px;top:60px;font-size:6.6px}
.card .contacts{position:absolute;left:0;right:0;top:82px;display:flex;flex-direction:column;gap:4px;font-size:14px}
.card .icon{width:11px;height:11px}

/* wide labels */
.label{left:737px;width:363px;height:121px}
.label-full{top:71px}
.label-phone{top:197px}
.label-email{top:322px}
.label-web{top:448px}
.label .brand-square{position:absolute;left:12px;top:15px;width:91px;height:91px}
.label .brand-name{position:absolute;left:115px;top:26px;font-size:40px}
.label .tagline{position:absolute;left:116px;top:64px;font-size:9.6px}
.label .pill{position:absolute;left:116px;top:80px;width:234px;height:26px;background:var(--navy);border-radius:3px;color:var(--paper);font-size:18px;font-weight:500;letter-spacing:.14em;display:flex;align-items:center;justify-content:center}
.label-full .contacts{position:absolute;left:116px;width:234px;top:79px;display:flex;flex-direction:column;align-items:center;gap:3px;font-size:10px}
.label-full .contacts .row{display:flex;gap:8px}
.label-full .icon{width:10px;height:10px;stroke:var(--orange)}
.label-full .contact-line{gap:5px}

/* long banner */
.banner{left:442px;top:591px;width:658px;height:185px}
.banner .brand-square{position:absolute;left:22px;top:43px;width:89px;height:89px}
.banner .brand-name{position:absolute;left:144px;top:46px;font-size:76px}
.banner .tagline{position:absolute;left:147px;top:114px;font-size:19.5px;letter-spacing:.13em}
.banner .contacts{position:absolute;left:24px;right:24px;top:147px;display:flex;justify-content:space-between;font-size:18px}
.banner .icon{width:18px;height:18px;stroke:var(--orange)}
</style>
</head>
<body>

<svg width="0" height="0" style="position:absolute" aria-hidden="true">
  <defs>
    <symbol id="i-phone" viewBox="0 0 24 24"><path d="M5 3h4l2 5-3 2a12 12 0 0 0 6 6l2-3 5 2v4a2 2 0 0 1-2 2A18 18 0 0 1 3 5a2 2 0 0 1 2-2z"/></symbol>
    <symbol id="i-mail" viewBox="0 0 24 24"><rect x="2" y="5" width="20" height="14"/><path d="M2 5l10 8 10-8M2 19l7-6M22 19l-7-6"/></symbol>
    <symbol id="i-web" viewBox="0 0 24 24"><circle cx="12" cy="12" r="10"/><path d="M2 12h20M12 2c3 3 4 6.5 4 10s-1 7-4 10c-3-3-4-6.5-4-10s1-7 4-10zM4 7h16M4 17h16"/></symbol>
  </defs>
</svg>

<!-- round sticker -->
<div class="sticker round">
  <svg class="rings" viewBox="0 0 282 282" width="282" height="282" aria-hidden="true">
    <g fill="none" stroke-width="6.5" stroke-linecap="round">
      <path d="M13.5 118.5 A129.5 129.5 0 0 1 219 37.6" stroke="var(--navy)"/>
      <path d="M231.8 48.7 A129.5 129.5 0 0 1 101.4 264.3" stroke="var(--green)"/>
      <path d="M11.8 148.9 A129.5 129.5 0 0 0 65.2 246" stroke="var(--orange)"/>
    </g>
  </svg>
  <div class="brand-square"></div>
  <div class="brand-name">Velunora</div>
  <div class="tagline"><span class="t-clean">CLEANING·</span><span class="t-garden">GARDENING·</span><span class="t-pest">PESTCONTROL</span></div>
  <div class="contacts">
    <div class="contact-line"><svg class="icon" width="11" height="11"><use href="#i-phone"/></svg>+39 331 5720418</div>
    <div class="contact-line"><svg class="icon" width="11" height="11"><use href="#i-mail"/></svg>office@velunora.srl</div>
    <div class="contact-line"><svg class="icon" width="11" height="11"><use href="#i-web"/></svg>www.velunora.srl</div>
  </div>
</div>

<!-- framed cards -->
<div class="sticker card card-navy">
  <div class="frame"></div>
  <div class="brand"><div class="brand-square"></div><div class="brand-name">Velunora</div></div>
  <div class="tagline"><span class="t-clean">CLEANING·</span><span class="t-garden">GARDENING·</span><span class="t-pest">PESTCONTROL</span></div>
  <div class="contacts">
    <div class="contact-line"><svg class="icon"><use href="#i-phone"/></svg>+39 331 5720418</div>
    <div class="contact-line"><svg class="icon"><use href="#i-mail"/></svg>office@velunora.srl</div>
    <div class="contact-line"><svg class="icon"><use href="#i-web"/></svg>www.velunora.srl</div>
  </div>
</div>

<div class="sticker card card-green">
  <div class="frame"></div>
  <div class="brand"><div class="brand-square"></div><div class="brand-name">Velunora</div></div>
  <div class="tagline"><span class="t-clean">CLEANING·</span><span class="t-garden">GARDENING·</span><span class="t-pest">PESTCONTROL</span></div>
  <div class="contacts">
    <div class="contact-line"><svg class="icon"><use href="#i-phone"/></svg>+39 331 5720418</div>
    <div class="contact-line"><svg class="icon"><use href="#i-mail"/></svg>office@velunora.srl</div>
    <div class="contact-line"><svg class="icon"><use href="#i-web"/></svg>www.velunora.srl</div>
  </div>
</div>

<div class="sticker card card-orange">
  <div class="frame"></div>
  <div class="brand"><div class="brand-square"></div><div class="brand-name">Velunora</div></div>
  <div class="tagline"><span class="t-clean">CLEANING·</span><span class="t-garden">GARDENING·</span><span class="t-pest">PESTCONTROL</span></div>
  <div class="contacts">
    <div class="contact-line"><svg class="icon"><use href="#i-phone"/></svg>+39 331 5720418</div>
    <div class="contact-line"><svg class="icon"><use href="#i-mail"/></svg>office@velunora.srl</div>
    <div class="contact-line"><svg class="icon"><use href="#i-web"/></svg>www.velunora.srl</div>
  </div>
</div>

<!-- wide labels -->
<div class="sticker label label-full">
  <div class="brand-square"></div>
  <div class="brand-name">Velunora</div>
  <div class="tagline"><span class="t-clean">CLEANING·</span><span class="t-garden">GARDENING·</span><span class="t-pest">PESTCONTROL</span></div>
  <div class="contacts">
    <div class="row">
      <div class="contact-line"><svg class="icon"><use href="#i-phone"/></svg>+39 331 5720418</div>
      <div class="contact-line"><svg class="icon"><use href="#i-mail"/></svg>office@velunora.srl</div>
    </div>
    <div class="contact-line"><svg class="icon"><use href="#i-web"/></svg>www.velunora.srl</div>
  </div>
</div>

<div class="sticker label label-phone">
  <div class="brand-square"></div>
  <div class="brand-name">Velunora</div>
  <div class="tagline"><span class="t-clean">CLEANING·</span><span class="t-garden">GARDENING·</span><span class="t-pest">PESTCONTROL</span></div>
  <div class="pill">+39 331 5720418</div>
</div>

<div class="sticker label label-email">
  <div class="brand-square"></div>
  <div class="brand-name">Velunora</div>
  <div class="tagline"><span class="t-clean">CLEANING·</span><span class="t-garden">GARDENING·</span><span class="t-pest">PESTCONTROL</span></div>
  <div class="pill">office@velunora.srl</div>
</div>

<div class="sticker label label-web">
  <div class="brand-square"></div>
  <div class="brand-name">Velunora</div>
  <div class="tagline"><span class="t-clean">CLEANING·</span><span class="t-garden">GARDENING·</span><span class="t-pest">PESTCONTROL</span></div>
  <div class="pill">www.velunora.srl</div>
</div>

<!-- long banner -->
<div class="sticker banner">
  <div class="brand-square"></div>
  <div class="brand-name">Velunora</div>
  <div class="tagline"><span class="t-clean">CLEANING·</span><span class="t-garden">GARDENING·</span><span class="t-pest">PESTCONTROL</span></div>
  <div class="contacts">
    <div class="contact-line"><svg class="icon"><use href="#i-phone"/></svg>+39 331 5720418</div>
    <div class="contact-line"><svg class="icon"><use href="#i-mail"/></svg>office@velunora.srl</div>
    <div class="contact-line"><svg class="icon"><use href="#i-web"/></svg>www.velunora.srl</div>
  </div>
</div>

</body>
</html>
```